Marketing , Sales and Distribution Website

This website/this business is specifically to start an international marketing, sales and distribution business - no more than 5 pages - one page design with supporting pages, a strong "call to action" design - lead generation design - Modern - can be easily upgraded.

Target Market(s)

Industrial, engineering, Art, technology, food products, fashion and accessories

Industry/Entity Type

Marketing

Coding

Coded - Design and coding required

Font styles to use
Sans Serif

Requirements
Must have
• user friendly. Fast upload time - space for content. Most have strategic "call to action" lead generation opportunities - space for video, links to social media. room for articles, blogs and upcoming tradeshows - modern interactive website - easy to upgrade in the future. Lastly a link or Tab to a one page site dedicated to mobile marketing subscriptions
Nice to have
• Client login area - backend CRM integration - Hubspot
• I am open to suggestions to make this site attractive for companies who import/export goods - or generate leads of companies who wish to import/export their products to the USA - a lot of this information is in the attachment.

```html
<!DOCTYPE html>
<html lang="en">
<head>
<meta charset="utf-8">
<title>Norvane Marketing</title>
<link href="https://fonts.googleapis.com/css2?family=Open+Sans:wght@300;400;600;700&display=swap" rel="stylesheet">
<style>
:root{
  --blue-deep:#1f3d8f;
  --blue:#2d4fb0;
  --blue-light:#4a72d1;
  --red:#ee3c4f;
  --red-dark:#d92c42;
  --dark:#2a2a2c;
  --ink:#222;
  --muted:#8c8c8c;
  --line:#c9d3ea;
  --soft:#f6f6f6;
  --white:#fff;
}
*{box-sizing:border-box;margin:0;padding:0}
html,body{width:1200px;height:3766px;overflow:hidden}
body{font-family:"Open Sans",Arial,sans-serif;color:var(--ink);background:var(--white);position:relative}
section,header,footer{position:absolute;left:0;width:1200px}
a{color:inherit;text-decoration:none}

/* hero */
.hero{top:0;height:602px;background:linear-gradient(160deg,#3a63c9 0%,#2447a8 45%,#1a3486 100%);overflow:hidden}
.hero-photo{position:absolute;inset:0;background:linear-gradient(115deg,rgba(120,160,240,.35) 0%,rgba(30,60,150,0) 40%,rgba(90,130,220,.3) 70%,rgba(20,40,120,.2) 100%)}
.brand{position:absolute;left:0;top:0;width:125px;height:125px;background:var(--blue-deep);display:flex;align-items:center;justify-content:center;color:var(--white);font-weight:600;font-size:20px}
.nav{position:absolute;left:183px;top:52px;display:flex;gap:30px;font-size:13px;font-weight:600;letter-spacing:.5px;color:var(--white)}
.nav .active{color:#a9bdf0;position:relative}
.nav .active::after{content:"";position:absolute;left:50%;top:24px;width:7px;height:7px;margin-left:-3px;border-radius:50%;background:var(--white)}
.phone{position:absolute;left:950px;top:52px;display:flex;align-items:center;gap:10px;color:var(--white);font-size:13px;font-weight:600}
.login{position:absolute;left:1164px;top:48px;width:28px;height:26px;background:#7e9be0;display:flex;align-items:center;justify-content:center}
.hero-copy{position:absolute;left:261px;top:232px;color:var(--white)}
.hero-copy h1{font-size:40px;font-weight:600;line-height:1.2}
.hero-copy p{font-size:21px;font-weight:300;line-height:1.3;margin-top:4px}
.btn{display:inline-flex;align-items:center;justify-content:center;border-radius:24px;font-size:12px;font-weight:600;letter-spacing:1.2px}
.btn-ghost{border:2px solid rgba(255,255,255,.8);color:var(--white)}
.hero-copy .btn{width:193px;height:46px;margin-top:40px}
.social-rail{position:absolute;left:1070px;top:236px;display:flex;flex-direction:column;gap:19px}
.social-rail span{width:22px;height:22px;border:1.5px solid rgba(255,255,255,.7);border-radius:50%;display:block}
.social-rail span.on{background:rgba(255,255,255,.75);transform:rotate(45deg);border-radius:3px}

/* big idea */
.big-idea{top:602px;height:415px;background:linear-gradient(120deg,var(--red) 0%,var(--red-dark) 100%)}
.rule{position:absolute;height:2px;width:176px;background:rgba(255,255,255,.7)}
.big-idea .rule{left:88px;top:71px}
.big-idea .copy{position:absolute;left:146px;top:100px;width:420px;color:var(--white)}
.big-idea h2{font-size:32px;font-weight:600}
.big-idea p{font-size:14px;line-height:1.55;margin-top:14px}
.big-idea .btn{width:148px;height:38px;margin-top:26px;font-size:11px}
.video{position:absolute;left:615px;top:0;width:439px;height:415px;background:linear-gradient(135deg,#e9edf2 0%,#9aa6b4 45%,#3b4657 100%)}
.video svg{position:absolute;left:180px;top:168px}

/* what we do */
.heading{position:absolute;left:0;width:1200px;text-align:center}
.heading h2{font-size:32px;font-weight:600;color:#222}
.heading p{font-size:13px;color:var(--muted);margin-top:2px}
.services{top:1017px;height:527px}
.services .heading{top:60px}
.cards{position:absolute;left:148px;top:153px;display:flex;width:904px;height:301px}
.card{position:relative;width:301px;height:301px;color:var(--white);text-align:center}
.card.road{background:linear-gradient(180deg,#c7d3de 0%,#8b949a 55%,#4f555a 100%)}
.card.work{background:linear-gradient(160deg,#6a6a6a 0%,#2a2a2a 100%);width:302px}
.card.deal{background:linear-gradient(200deg,#5a6f8e 0%,#9aa6b6 50%,#6a6f78 100%)}
.card .label{position:absolute;left:0;right:0;bottom:50px;font-size:20px}
.card.work .label{position:static;margin-top:110px}
.card.work p{font-size:13px;line-height:1.4;margin:10px 40px 0}
.card.work .btn{background:#7e9be0;width:148px;height:36px;margin-top:16px;font-size:11px}

/* testimonials */
.testimonials{top:1544px;height:414px;background:linear-gradient(120deg,#343436 0%,#262628 100%);color:var(--white)}
.testimonials .rule{left:88px;top:73px;background:rgba(255,255,255,.5)}
.testimonials .copy{position:absolute;left:146px;top:102px;width:600px}
.testimonials h2{font-size:32px;font-weight:600}
.testimonials blockquote{font-size:14px;line-height:1.55;margin-top:14px}
.testimonials .name{font-size:14px;margin-top:36px}
.testimonials .place{font-size:13px;color:#bbb}
.avatar{position:absolute;left:876px;top:113px;width:176px;height:176px;border-radius:50%;border:6px solid rgba(255,255,255,.85);background:radial-gradient(circle at 50% 40%,#c89a7e 0%,#6b4a3a 60%,#8fb0a0 100%)}
.dots{position:absolute;left:932px;top:322px;display:flex;gap:8px}
.dots span{width:8px;height:8px;border:1px solid #ccc;transform:rotate(45deg)}
.dots span.on{background:#fff}

/* blog */
.blog{top:1958px;height:672px}
.blog .heading{top:68px}
.post{position:absolute;top:163px;width:440px}
.post.one{left:148px}
.post.two{left:612px}
.thumb{height:183px}
.thumb.laptop{background:linear-gradient(160deg,#eef1f5 0%,#9aa3ad 50%,#2a2c30 100%)}
.thumb.leaf{background:linear-gradient(135deg,#b9e37a 0%,#5aa32c 50%,#2f6c17 100%)}
.meta{font-size:12px;color:var(--red);margin-top:26px}
.post h3{font-size:19px;font-weight:400;line-height:1.3;margin-top:8px;color:#222}
.post.one h3{text-decoration:underline}
.post p{font-size:13px;line-height:1.55;color:#777;margin-top:14px}
.post .btn{width:148px;height:36px;margin-top:28px;font-size:11px}
.btn-line{border:1.5px solid var(--line);color:#a9b8dc}
.btn-fill{background:#89a2dd;color:var(--white)}

/* news */
.news{top:2630px;height:337px;background:var(--soft)}
.news .rule{left:88px;top:75px;background:#bbb}
.news h2{position:absolute;left:146px;top:104px;font-size:32px;font-weight:600}
.news-item{position:absolute;top:170px;width:250px}
.news-item time{font-size:12px;color:var(--red)}
.news-item p{font-size:15px;line-height:1.45;margin-top:8px}
.news-item.linked p{text-decoration:underline}

/* contact */
.contact{top:2967px;height:384px;background:linear-gradient(120deg,var(--blue) 0%,#22398a 100%);color:var(--white)}
.contact .rule{left:88px;top:75px;background:rgba(255,255,255,.6)}
.contact h2{position:absolute;left:146px;top:104px;font-size:32px;font-weight:600}
.contact .socials{position:absolute;left:150px;top:177px;display:flex;gap:19px}
.contact .socials span{width:20px;height:20px;border:1.5px solid rgba(255,255,255,.8);transform:rotate(45deg);display:block}
.contact .details{position:absolute;left:447px;top:168px;font-size:14px;line-height:1.5}
.contact .details strong{font-weight:600}
.contact .details .call{font-size:21px;margin-top:8px}
.contact .details .addr{margin-top:14px}
.contact .legal{position:absolute;left:750px;top:168px;font-size:14px;line-height:1.5}
.contact .legal a{display:block;margin-top:18px}

/* map */
.map{top:3351px;height:415px;background:linear-gradient(180deg,#ececec 0%,#dcdcdc 100%)}
.map svg{position:absolute;left:584px;top:176px}
</style>
</head>
<body>

<header class="hero">
  <div class="hero-photo" role="img" aria-label="City skyscrapers photographed from below, tinted blue"></div>
  <a class="brand" href="#">Norvane</a>
  <nav class="nav">
    <a href="#">NORVANE</a>
    <a href="#" class="active">DISTRIBUTION</a>
    <a href="#">MARKETING</a>
    <a href="#">SALES</a>
    <a href="#">NEWS</a>
    <a href="#">CONTACT US</a>
  </nav>
  <div class="phone">
    <svg width="16" height="16" viewBox="0 0 24 24"><path d="M6.6 10.8a15 15 0 0 0 6.6 6.6l2.2-2.2c.3-.3.7-.4 1-.2 1.1.4 2.3.6 3.6.6.6 0 1 .4 1 1V20c0 .6-.4 1-1 1A17 17 0 0 1 3 4c0-.6.4-1 1-1h3.5c.6 0 1 .4 1 1 0 1.3.2 2.5.6 3.6.1.3 0 .7-.2 1z" fill="#fff"/></svg>
    +1 555-014-2290
  </div>
  <a class="login" href="#" aria-label="Client login">
    <svg width="14" height="14" viewBox="0 0 14 14"><path d="M7 1 13 12H1z" fill="none" stroke="#fff" stroke-width="1.5"/></svg>
  </a>
  <div class="hero-copy">
    <h1>Norvane Marketing</h1>
    <p>Product marketing, sales and distribution<br>full service marketing agency</p>
    <a class="btn btn-ghost" href="#">EXPLORE MORE</a>
  </div>
  <div class="social-rail" aria-label="Social links">
    <span></span><span class="on"></span><span></span><span></span><span></span>
  </div>
</header>

<section class="big-idea">
  <div class="rule"></div>
  <div class="copy">
    <h2>Big Idea</h2>
    <p>If your plans include developing sales collateral,<br>launching a new product, or redesigning a web site,<br>you will want to know how Norvane can help you<br>Utilizing creative flair and award winning<br>agency.</p>
    <a class="btn btn-ghost" href="#">LEARN MORE</a>
  </div>
  <div class="video" role="img" aria-label="Video still of two businessmen reviewing work at a laptop">
    <svg width="80" height="80" viewBox="0 0 80 80"><circle cx="40" cy="40" r="38" fill="rgba(255,255,255,.45)"/><path d="M32 24 56 40 32 56z" fill="#fff"/></svg>
  </div>
</section>

<section class="services">
  <div class="heading">
    <h2>What We Do</h2>
    <p>Service we provided in those categories</p>
  </div>
  <div class="cards">
    <div class="card road" role="img" aria-label="Open road with yellow direction signs"><span class="label">Distribution</span></div>
    <div class="card work" role="img" aria-label="Hands working on a laptop, darkened">
      <div class="label">Marketing</div>
      <p>On/Off shelf marketing, creating a demand lorem impsum</p>
      <a class="btn" href="#">LEARN MORE</a>
    </div>
    <div class="card deal" role="img" aria-label="Business handshake"><span class="label">Sales</span></div>
  </div>
</section>

<section class="testimonials">
  <div class="rule"></div>
  <div class="copy">
    <h2>Testimonials</h2>
    <blockquote>Thank you very much. I'm impressed with your service. With years of marketing and advertising experience, we are focused on creating strategical communication combined with speed and timely delivery within budget. I've already told my friends about your company and your quick response, thanks again!</blockquote>
    <div class="name">Dana Merrit</div>
    <div class="place">USA</div>
  </div>
  <div class="avatar" role="img" aria-label="Portrait photo of the client"></div>
  <div class="dots"><span></span><span class="on"></span><span></span><span></span></div>
</section>

<section class="blog">
  <div class="heading">
    <h2>Latest Blog</h2>
    <p>The official blog of Norvane Marketing</p>
  </div>
  <article class="post one">
    <div class="thumb laptop" role="img" aria-label="Laptop keyboard with a payment card"></div>
    <div class="meta">18.05.2016 &nbsp;|&nbsp; BY ADMIN</div>
    <h3>Complete Guide to the E-Commerce &amp;<br>Internet Business</h3>
    <p>Working in a business field that's as competitive as our is (legal help), we needed some extra piece of analytics real bad... Thankfully, hiring this company to do all...</p>
    <a class="btn btn-line" href="#">READ MORE</a>
  </article>
  <article class="post two">
    <div class="thumb leaf" role="img" aria-label="Hand holding a small globe on a green leaf"></div>
    <div class="meta">18.05.2016 &nbsp;|&nbsp; BY ADMIN</div>
    <h3>Complete Guide to the Technology<br>(CleanTech) Industry</h3>
    <p>Working in a business field that's as competitive as our is (legal help), we needed some extra piece of analytics real bad... Thankfully, hiring this company to do all...</p>
    <a class="btn btn-fill" href="#">READ MORE</a>
  </article>
</section>

<section class="news">
  <div class="rule"></div>
  <h2>News and Updates</h2>
  <div class="news-item" style="left:146px"><time>16.06.2016</time><p>We guess there's no need to ex-plain, just how important the hardware ...</p></div>
  <div class="news-item linked" style="left:449px"><time>17.05.2016</time><p>Doing business research for all fields, we post the overviews for the reviewed ...</p></div>
  <div class="news-item" style="left:750px"><time>16.06.2016</time><p>Over the last decade or so, the alternative energy movement has quickly ...</p></div>
</section>

<footer class="contact">
  <div class="rule"></div>
  <h2>Get in touch with us</h2>
  <div class="socials" aria-label="Social links"><span></span><span></span><span></span><span></span><span></span></div>
  <div class="details">
    <strong>Contact Us</strong>
    <div class="call">Call: +1 555-014-2290</div>
    <div>info@norvanemarketing.com</div>
    <div class="addr">1820 Harbor Lane Fairview,<br>WA 98000</div>
  </div>
  <div class="legal">
    <div>© 2017 Norvane Marketing.<br>All rights reserved.</div>
    <a href="#">Privacy Policy</a>
  </div>
</footer>

<section class="map" role="img" aria-label="Grey street map of the office area">
  <svg width="28" height="40" viewBox="0 0 28 40"><path d="M14 0C6 0 0 6 0 14c0 10 14 26 14 26s14-16 14-26C28 6 22 0 14 0z" fill="#1f3d8f"/><circle cx="14" cy="14" r="5" fill="#fff"/></svg>
</section>

</body>
</html>
```